Business Card Design Project

Hello- I am an interior stylist/product designer whose work is detail driven, very clean and transitional in style and I want my business card to reflect those qualities. I have a logo that I use on my website- my name and a hand drawn chandelier that I want incorporated into the design. However, "Design for the Home" needs to be changed to "Designs". I will be using cream colored stock and am thinking of gray text and logo. I need your help in pulling my card together since it will be the most used element and drive the design of the rest of my stationary suite.
Updates

Please note that I have changed my QR code from my cell # to my website. The new code will be downloaded now.

Reason: I want to thank everyone who has submitted designs- there are truly some very inspiring designs and I am very pleased. I want to make certain that I get this right and have an attractive and highly effective marketing tool when we are finished. With that said, I have run into a technical problem with one aspect of the card- a qr code for my website that was not part of the original brief. I will get that corrected today and post. Once I get that taken care of, I will post comments to all designs received do far. Thanks again for everyone's efforts, Risa

QR Code for the website is now uploaded. Thanks for your patience!

Target Market(s)

Upper middle class- mostly women

Industry/Entity Type

Business

Requirements
Must have
• Marisa Vantry Designs
"...to the last detail."
214-555-0148
marisavantry@plumwick.net
www.marisavantrydesigns-example.com
27083 Birchmont Court
Dallas, TX 75000
Nice to have
• Risa Vantry
Owner

```html
<!DOCTYPE html>
<html lang="en">
<head>
<meta charset="utf-8">
<title>Marisa Vantry Designs – Business Card</title>
<link rel="stylesheet" href="https://fonts.googleapis.com/css2?family=Cormorant+Garamond:wght@400&family=Didact+Gothic&display=swap">
<style>
  :root {
    --backdrop: #d9d9d9;
    --card: #f6f6f5;
    --band: #ececeb;
    --pattern-light: #e9e9e8;
    --pattern-dark: #dcdcdb;
    --ink: #5c5c5c;
    --ink-soft: #8a8a8a;
  }
  * { margin: 0; padding: 0; box-sizing: border-box; }
  html, body {
    width: 1200px;
    height: 880px;
    overflow: hidden;
    background: var(--backdrop);
  }
  .canvas {
    width: 1200px;
    height: 880px;
    display: flex;
    align-items: center;
    justify-content: center;
  }
  .card {
    position: relative;
    width: 1050px;
    height: 600px;
    background: var(--card);
    border-radius: 42px;
    overflow: hidden;
    box-shadow: 0 6px 24px rgba(0,0,0,0.12);
  }
  .pattern {
    position: absolute;
    left: 0;
    width: 100%;
    background: linear-gradient(135deg, var(--pattern-light), var(--pattern-dark) 50%, var(--pattern-light));
  }
  .pattern--top { top: 0; height: 190px; }
  .pattern--bottom { bottom: 0; height: 170px; }
  .band {
    position: absolute;
    left: 0;
    top: 190px;
    width: 100%;
    height: 240px;
    background: var(--band);
    display: flex;
    align-items: center;
    justify-content: space-between;
    padding: 0 90px 0 80px;
  }
  .brand {
    display: flex;
    flex-direction: column;
    align-items: center;
    gap: 10px;
  }
  .brand__name {
    font-family: "Cormorant Garamond", serif;
    font-weight: 400;
    font-size: 60px;
    line-height: 1;
    color: var(--ink);
    letter-spacing: 1px;
    display: flex;
    align-items: center;
    gap: 18px;
  }
  .brand__mark {
    width: 14px;
    height: 14px;
    border-radius: 50%;
    background: var(--ink-soft);
  }
  .brand__designs {
    font-family: "Didact Gothic", sans-serif;
    font-size: 15px;
    letter-spacing: 8px;
    padding-left: 8px;
    color: var(--ink-soft);
  }
  .brand__slogan {
    font-family: "Cormorant Garamond", serif;
    font-size: 20px;
    letter-spacing: 1px;
    color: var(--ink);
    margin-top: 2px;
  }
  .contact {
    font-family: "Didact Gothic", sans-serif;
    font-style: normal;
    font-size: 17px;
    line-height: 1.55;
    color: var(--ink-soft);
  }
  .contact__name { color: var(--ink); font-size: 20px; }
  .contact__role { margin-bottom: 10px; }
</style>
</head>
<body>
<main class="canvas">
  <article class="card">
    <div class="pattern pattern--top" role="img" aria-label="Faint grey repeating chandelier-motif pattern"></div>
    <section class="band">
      <div class="brand">
        <div class="brand__name">Marisa <span class="brand__mark"></span> Vantry</div>
        <div class="brand__designs">DESIGNS</div>
        <div class="brand__slogan">...to the last detail.</div>
      </div>
      <address class="contact">
        <div class="contact__name">Risa Vantry</div>
        <div class="contact__role">Owner</div>
        <div>27083 Birchmont Court</div>
        <div>Dallas, TX 75000</div>
        <div>p: 214-555-0148</div>
        <div>e: marisavantry@plumwick.net</div>
        <div>w: www.marisavantrydesigns-example.com</div>
      </address>
    </section>
    <div class="pattern pattern--bottom" role="img" aria-label="Faint grey repeating chandelier-motif pattern"></div>
  </article>
</main>
</body>
</html>
```